QM Studios needs and Interior Design Business card

I can do anything from Commercial to Residential and Free lance. Beginning to end in design selection process.
Need something to catch the eye of potential customers and vendors. From furniture to Tile and Cabinet selections. I can do it all.

Industry/Entity Type

Design Agency

Contact Information for Business Card

QM Studios- Design Consultanting Residential, Commerical
Maybe a cool detail background. Wall paper print that can have some texture

Font styles to use
Serif

Colors
709dcb
34a6d7
b868aa
e667a6
f59296
85acd3
ffffff
000000
5c5c5c

Requirements
Must have
• Square or Rectangular with Rounded edges
• Name
• Address
• Phone
• Email
Nice to have
• Some colored edges More simples not too busy
• Pattern detail in background.
Should not have
• Not too much color

```html
<!DOCTYPE html>
<html lang="en">
<head>
<meta charset="utf-8">
<title>QM Studios – Business Card</title>
<link rel="stylesheet" href="https://fonts.googleapis.com/css2?family=PT+Serif:wght@400;700&display=swap">
<style>
  :root {
    --backdrop: #8e8f90;
    --card-white: #ffffff;
    --brand-blue: #709dcb;
    --accent-pink: #b868aa;
    --ink: #5c5c5c;
    --rule: #85acd3;
    --on-blue: #ffffff;
  }
  * { box-sizing: border-box; margin: 0; padding: 0; }
  html, body { width: 1105px; height: 1200px; overflow: hidden; }
  body {
    background: var(--backdrop);
    font-family: "PT Serif", Georgia, "Times New Roman", serif;
    position: relative;
  }
  .card {
    position: absolute;
    left: 182px;
    width: 747px;
    height: 427px;
    border-radius: 12px;
  }
  .card--front { top: 119px; background: var(--card-white); }
  .card--back  { top: 637px; background: var(--brand-blue); }

  /* Front */
  .brand-mark {
    position: absolute;
    left: 322px; top: 52px;
    width: 118px; height: 118px;
  }
  .brand-name {
    position: absolute;
    left: 0; right: 0; top: 184px;
    text-align: center;
    color: var(--brand-blue);
    font-size: 33px;
    font-weight: 400;
    letter-spacing: 5px;
  }
  .person {
    position: absolute;
    right: 413px; top: 292px;
    text-align: right;
  }
  .person__name {
    color: var(--accent-pink);
    font-weight: 700;
    font-size: 25px;
    line-height: 32px;
  }
  .person__title {
    color: var(--ink);
    font-size: 20px;
    line-height: 28px;
  }
  .divider {
    position: absolute;
    left: 360px; top: 262px;
    width: 2px; height: 122px;
    background: var(--rule);
  }
  .contact-list {
    position: absolute;
    left: 387px; top: 266px;
    list-style: none;
  }
  .contact-list li {
    display: flex;
    align-items: center;
    height: 28.5px;
    color: var(--ink);
    font-size: 18px;
    white-space: nowrap;
  }
  .contact-list svg {
    width: 17px; height: 17px;
    margin-right: 10px;
    fill: var(--brand-blue);
    flex: none;
  }

  /* Back */
  .back-mark {
    position: absolute;
    left: 268px; top: 96px;
    width: 210px; height: 210px;
    border: 6px solid var(--on-blue);
    border-radius: 50%;
    display: flex;
    align-items: center;
    justify-content: center;
  }
  .back-mark__name {
    color: var(--on-blue);
    font-size: 28px;
    letter-spacing: 1px;
  }
  .services {
    position: absolute;
    left: 0; right: 0; top: 352px;
    text-align: center;
    color: var(--on-blue);
    font-size: 20px;
  }
</style>
</head>
<body>
  <section class="card card--front">
    <svg class="brand-mark" viewBox="0 0 118 118" aria-hidden="true">
      <circle cx="59" cy="59" r="55" fill="none" stroke="var(--brand-blue)" stroke-width="5"/>
    </svg>
    <h1 class="brand-name">QM Studios</h1>

    <div class="person">
      <p class="person__name">Nora Castell</p>
      <p class="person__title">Design Consultant</p>
    </div>

    <div class="divider"></div>

    <ul class="contact-list">
      <li>
        <svg viewBox="0 0 24 24" aria-hidden="true"><path d="M6.6 10.8a15.1 15.1 0 0 0 6.6 6.6l2.2-2.2a1 1 0 0 1 1-.25 11.4 11.4 0 0 0 3.6.57 1 1 0 0 1 1 1V20a1 1 0 0 1-1 1A17 17 0 0 1 3 4a1 1 0 0 1 1-1h3.5a1 1 0 0 1 1 1c0 1.25.2 2.450.57 3.57a1 1 0 0 1-.25 1z"/></svg>
        555 014 2738
      </li>
      <li>
        <svg viewBox="0 0 24 24" aria-hidden="true"><path d="M2 5h20v14H2z"/><path d="M2 5l10 8 10-8" fill="none" stroke="var(--card-white)" stroke-width="2"/></svg>
        hello@qmstudios.com
      </li>
      <li>
        <svg viewBox="0 0 24 24" aria-hidden="true"><circle cx="12" cy="12" r="10"/><path d="M2 12h20M12 2c3 3 3 17 0 20M12 2c-3 3-3 17 0 20" fill="none" stroke="var(--card-white)" stroke-width="1.6"/></svg>
        www.qmstudios.com
      </li>
      <li>
        <svg viewBox="0 0 24 24" aria-hidden="true"><path d="M12 2a7 7 0 0 0-7 7c0 5.2 7 13 7 13s7-7.8 7-13a7 7 0 0 0-7-7z"/><circle cx="12" cy="9" r="2.6" fill="var(--card-white)"/></svg>
        214 Alder Lane, Portland, OR
      </li>
    </ul>
  </section>

  <section class="card card--back">
    <div class="back-mark">
      <span class="back-mark__name">QM Studios</span>
    </div>
    <p class="services">Design Consulting • Commercial • Residential</p>
  </section>
</body>
</html>
```